Harbourline Refrigeration business card design

We would like a new design for our business card as we have a new logo.
We need generic business card to give our customers with our office details - with the option of making it individualized for each manager

Target Market(s)

Companies and homeowners

Industry/Entity Type

Air Conditioning

Contact Information for Business Card

We are not sure if we want single or double sided it will depend on the design we choose

Colors
33a6d7
0255a3

Requirements
Must have
• Logo
• phone: (08) 8721 5940
• email: harbourserve@tealnet.example
• website: www.harbourlinerefrigeration.example
• AU61420
• BLD472913
Nice to have
• Address - Shed 5/284 Tallis Rd, Kestrel Bay SA 5617

```html
<!DOCTYPE html>
<html lang="en">
<head>
<meta charset="utf-8">
<title>Harbourline Refrigeration – Business Card</title>
<link href="https://fonts.googleapis.com/css2?family=Lato:wght@400;700&display=swap" rel="stylesheet">
<style>
  :root {
    --navy: #1b3f78;
    --brand-blue: #0255a3;
    --sky: #33a6d7;
    --sky-soft: #8fcbe8;
    --ink: #3a3a3a;
    --paper: #ffffff;
    --backdrop: #ffffff;
  }
  * { box-sizing: border-box; margin: 0; padding: 0; }
  html, body {
    width: 1200px; height: 1200px; overflow: hidden;
    background: var(--backdrop);
    font-family: "Lato", sans-serif;
  }
  .card {
    position: absolute; left: 246px; width: 708px; height: 404px;
    background: var(--paper); border-radius: 22px; overflow: hidden;
    box-shadow: 6px 10px 14px rgba(0,0,0,0.28);
  }
  .card--front { top: 138px; }
  .card--back { top: 646px; }

  .brand-dot {
    position: absolute; border-radius: 50%; background: var(--sky-soft); opacity: 0.55;
  }
  .brand-dot--upper { left: 40px; top: 26px; width: 118px; height: 118px; }
  .brand-dot--lower { left: 40px; top: 254px; width: 118px; height: 118px; }

  .wordmark {
    position: absolute; color: var(--navy);
    font-weight: 700; line-height: 1.02; letter-spacing: -0.5px;
  }
  .card--front .wordmark { right: 40px; top: 150px; font-size: 34px; text-align: right; }
  .card--back .wordmark { left: 380px; top: 100px; font-size: 28px; text-align: left; }
  .wordmark__dot {
    display: block; width: 44px; height: 44px; border-radius: 50%;
    background: var(--sky); margin: 0 0 8px auto;
  }
  .card--back .wordmark__dot { width: 38px; height: 38px; margin: 0 auto 8px; }

  .licences {
    position: absolute; right: 38px; top: 354px; display: flex; gap: 20px;
    font-size: 17px; color: var(--sky);
  }
  .licence { display: flex; align-items: center; gap: 7px; }
  .licence__mark {
    width: 14px; height: 14px; border-radius: 50%; border: 3px solid var(--navy);
  }

  .holder { position: absolute; left: 36px; top: 98px; }
  .holder__name { font-size: 28px; font-weight: 700; color: var(--navy); }
  .holder__role { font-size: 22px; font-weight: 700; color: var(--sky); margin-top: 2px; }

  .contacts { position: absolute; left: 38px; top: 250px; list-style: none; }
  .contacts li {
    display: flex; align-items: center; gap: 12px;
    font-size: 17px; color: var(--ink); height: 25px;
  }
  .contacts svg { width: 16px; height: 16px; fill: var(--sky); flex: none; }

  .wave { position: absolute; left: 0; top: 0; width: 708px; height: 404px; }

  .address {
    position: absolute; right: 38px; top: 330px; text-align: right;
    color: var(--paper); font-size: 17px; line-height: 25px;
  }
</style>
</head>
<body>

<section class="card card--front" aria-label="Card front">
  <span class="brand-dot brand-dot--upper"></span>
  <span class="brand-dot brand-dot--lower"></span>
  <div class="wordmark"><span class="wordmark__dot"></span>Harbourline<br>Refrigeration</div>
  <div class="licences">
    <span class="licence"><span class="licence__mark"></span>AU61420</span>
    <span class="licence"><span class="licence__mark"></span>BLD472913</span>
  </div>
</section>

<section class="card card--back" aria-label="Card back">
  <svg class="wave" viewBox="0 0 708 404" aria-hidden="true">
    <path d="M0,348 C150,362 320,356 450,330 C330,362 160,374 0,372 Z" fill="var(--sky)"/>
    <path d="M0,404 L0,386 C250,394 470,372 708,240 L708,404 Z" fill="var(--navy)"/>
  </svg>

  <div class="holder">
    <p class="holder__name">Daniel Whitcombe</p>
    <p class="holder__role">Manager</p>
  </div>

  <div class="wordmark"><span class="wordmark__dot"></span>Harbourline<br>Refrigeration</div>

  <ul class="contacts">
    <li><svg viewBox="0 0 24 24"><path d="M6.6 10.8c1.4 2.8 3.8 5.1 6.6 6.6l2.2-2.2c.3-.3.7-.4 1-.2 1.1.4 2.3.6 3.6.6.6 0 1 .4 1 1V20c0 .6-.4 1-1 1C10.6 21 3 13.4 3 4c0-.6.4-1 1-1h3.5c.6 0 1 .4 1 1 0 1.3.2 2.5.6 3.6.1.3 0 .7-.2 1z"/></svg>(08) 8721 5940</li>
    <li><svg viewBox="0 0 24 24"><path d="M2 5h20v14H2z M3 6l9 7 9-7" stroke="#fff" stroke-width="1.6"/></svg>harbourserve@tealnet.example</li>
    <li><svg viewBox="0 0 24 24"><circle cx="12" cy="12" r="9.5"/><path d="M2.5 12h19M12 2.5v19M12 2.5c-3.5 3-3.5 16 0 19M12 2.5c3.5 3 3.5 16 0 19" stroke="#fff" stroke-width="1.3" fill="none"/></svg>www.harbourlinerefrigeration.example</li>
  </ul>

  <p class="address">Shed 5/284 Tallis Rd<br>Kestrel Bay SA 5617</p>
</section>

</body>
</html>
```